Business card design needed

We require business cards for our young and innovative construction team.

Our business is Brask Constructions and we have used Lime, Navy and white with our colours so far.

We would like business cards that show our passion for perfection and detail, communication and management.

Looking forward to seeing the deigns!!

Contact Information for Business Card

Dan Pellow
Brask Constructions Pty Ltd
PO Box 782 Quarrow Flats NSW 2795
Mobile: 0471 392 608
Email: dpellow@braskconstructions.com.au
Web: www.braskconstructions.com.au

```html
<!DOCTYPE html>
<html lang="en">
<head>
<meta charset="utf-8">
<title>Brask Constructions – Business Card</title>
<link href="https://fonts.googleapis.com/css2?family=Mulish:wght@400;700;800&display=swap" rel="stylesheet">
<style>
  :root {
    --backdrop: #2f3033;
    --navy: #3c5283;
    --navy-ink: #3a4f7c;
    --lime: #8cc63f;
    --paper: #eeeeec;
    --paper-ink: #ffffff;
    --muted: #9a9fa8;
  }
  * { margin: 0; padding: 0; box-sizing: border-box; }
  html, body { width: 1200px; height: 900px; overflow: hidden; }
  body {
    background: var(--backdrop);
    font-family: "Mulish", "Century Gothic", sans-serif;
    display: flex;
    flex-direction: column;
    align-items: center;
    justify-content: center;
    gap: 56px;
  }
  .card {
    width: 630px;
    height: 360px;
    border-radius: 4px;
    position: relative;
    box-shadow: 0 14px 30px rgba(0,0,0,.45);
  }
  .card--front { background: var(--paper); color: var(--navy-ink); padding: 46px 52px; }
  .card--back { background: var(--navy); display: flex; align-items: center; justify-content: center; }

  .wordmark { display: flex; align-items: center; gap: 14px; }
  .wordmark__square { width: 26px; height: 26px; background: var(--lime); }
  .wordmark__name {
    font-weight: 700;
    font-size: 38px;
    letter-spacing: 1px;
    color: var(--navy-ink);
    line-height: 1;
  }
  .card--back .wordmark__name { color: var(--paper-ink); font-size: 42px; }

  .licence {
    position: absolute;
    right: 52px;
    top: 100px;
    font-size: 12px;
    color: var(--muted);
  }

  .holder {
    margin-top: 44px;
    font-weight: 800;
    font-size: 22px;
    color: var(--navy-ink);
  }
  .contacts { list-style: none; margin-top: 16px; }
  .contacts li {
    display: flex;
    align-items: center;
    gap: 12px;
    font-size: 17px;
    line-height: 1.65;
    color: var(--navy-ink);
  }
  .contacts svg { width: 18px; height: 18px; flex: none; }
</style>
</head>
<body>
  <section class="card card--front" aria-label="Business card front">
    <div class="wordmark">
      <span class="wordmark__square"></span>
      <span class="wordmark__name">Brask Constructions</span>
    </div>
    <p class="licence">Lic. 481307C</p>
    <h1 class="holder">Dan Pellow</h1>
    <ul class="contacts">
      <li>
        <svg viewBox="0 0 20 20" aria-hidden="true"><circle cx="10" cy="10" r="10" fill="#8cc63f"/><rect x="7" y="4.5" width="6" height="11" rx="1.2" fill="none" stroke="#fff" stroke-width="1.5"/></svg>
        0471 392 608
      </li>
      <li>
        <svg viewBox="0 0 20 20" aria-hidden="true"><circle cx="10" cy="10" r="10" fill="#8cc63f"/><rect x="5" y="6.5" width="10" height="7" fill="none" stroke="#fff" stroke-width="1.4"/><path d="M5 6.5 10 10.5 15 6.5" fill="none" stroke="#fff" stroke-width="1.4"/></svg>
        dpellow@braskconstructions.com.au
      </li>
      <li>
        <svg viewBox="0 0 20 20" aria-hidden="true"><circle cx="10" cy="10" r="10" fill="#8cc63f"/><circle cx="10" cy="10" r="5" fill="none" stroke="#fff" stroke-width="1.3"/><path d="M5 10h10M10 5c-2.4 2.8-2.4 7.2 0 10M10 5c2.4 2.8 2.4 7.2 0 10" fill="none" stroke="#fff" stroke-width="1.1"/></svg>
        www.braskconstructions.com.au
      </li>
      <li>
        <svg viewBox="0 0 20 20" aria-hidden="true"><circle cx="10" cy="10" r="10" fill="#8cc63f"/><path d="M10 4.5a3.5 3.5 0 0 0-3.5 3.5c0 2.8 3.5 7 3.5 7s3.5-4.2 3.5-7A3.5 3.5 0 0 0 10 4.5z" fill="#fff"/><circle cx="10" cy="8" r="1.3" fill="#8cc63f"/></svg>
        PO Box 782 Quarrow Flats, NSW 2795
      </li>
    </ul>
  </section>

  <section class="card card--back" aria-label="Business card back">
    <div class="wordmark">
      <span class="wordmark__square"></span>
      <span class="wordmark__name">Brask Constructions</span>
    </div>
  </section>
</body>
</html>
```